Fern Hollow Animal Hospital Postcard Design

I need a postcard for grand opening. The front of the card should have our business name and logo, below the logo I want to have a coupon for " Free office visit or $ 20 off of packages " for the first time clients.

I want to have the packages prices and details on the back of the postcard, the details of the packages are attached.

```html
<!DOCTYPE html>
<html lang="en">
<head>
<meta charset="utf-8">
<title>Fern Hollow Animal Hospital – Grand Opening</title>
<link href="https://fonts.googleapis.com/css2?family=Antonio:wght@100;400;700&family=Oswald:wght@400;500&display=swap" rel="stylesheet">
<style>
  :root{
    --sky:#a9d7e6;
    --teal:#2ba7c4;
    --coupon-teal:#2eaab6;
    --green:#7ab833;
    --coupon-green:#6bbd3a;
    --orange:#f39a1e;
    --ink:#1d1d1d;
    --white:#ffffff;
    --fur-dark:#3a2a1e;
    --fur-tan:#b9824a;
    --fur-light:#e2c9a6;
  }
  *{margin:0;padding:0;box-sizing:border-box}
  html,body{width:1200px;height:600px;overflow:hidden;background:var(--white)}
  .postcard{position:relative;width:1200px;height:600px;overflow:hidden;background:var(--white);font-family:"Oswald",sans-serif}

  .pet-photo{
    position:absolute;left:560px;top:70px;width:640px;height:530px;
    background:
      radial-gradient(ellipse 38% 30% at 55% 36%, var(--fur-tan) 0%, rgba(185,130,74,.7) 55%, rgba(185,130,74,0) 100%),
      radial-gradient(ellipse 50% 55% at 60% 80%, var(--fur-dark) 0%, rgba(58,42,30,.85) 50%, rgba(58,42,30,0) 100%),
      radial-gradient(ellipse 45% 48% at 55% 45%, var(--fur-light) 0%, rgba(226,201,166,0) 100%);
  }

  .headline{
    position:absolute;left:40px;top:14px;
    font-family:"Antonio",sans-serif;font-weight:100;
    font-size:154px;line-height:1;letter-spacing:2px;
    color:var(--sky);white-space:nowrap;
  }

  .event-info{position:absolute;left:1014px;top:30px;font-family:"Antonio",sans-serif;line-height:1.1}
  .event-date{color:var(--teal);font-size:33px;font-weight:400}
  .event-time{color:var(--green);font-size:33px;font-weight:400}
  .event-address{color:var(--green);font-size:17px;font-weight:700;letter-spacing:.5px;margin-top:4px;word-spacing:5px}

  .brand{position:absolute;left:122px;top:200px;display:flex;align-items:center;gap:16px}
  .brand-mark{width:22px;height:22px;border-radius:50%;background:var(--teal)}
  .brand-name{font-family:"Antonio",sans-serif;font-weight:700;color:var(--teal);font-size:44px;line-height:1.05;letter-spacing:1px;text-transform:uppercase}

  .divider{position:absolute;left:14px;top:325px;width:636px;border-top:2px dashed #555}

  .website{position:absolute;left:982px;top:310px;font-family:"Oswald",sans-serif;font-size:11px;letter-spacing:4px;color:var(--ink)}

  .coupon{position:absolute;width:260px;height:240px}
  .coupon svg{position:absolute;inset:0}
  .coupon-text{position:absolute;inset:0;display:flex;flex-direction:column;align-items:center;justify-content:center;color:var(--white);font-family:"Antonio",sans-serif;text-transform:uppercase}
  .coupon-free{left:92px;top:340px}
  .coupon-free .big{font-size:66px;font-weight:400;line-height:1}
  .coupon-free .small{font-size:23px;font-weight:700;margin-top:2px}
  .coupon-package{left:378px;top:338px}
  .coupon-package .amount{display:flex;align-items:flex-end;line-height:1}
  .coupon-package .dollar{font-size:32px;align-self:flex-start;margin-top:10px}
  .coupon-package .big{font-size:66px}
  .coupon-package .off{font-size:34px;margin-left:4px;margin-bottom:4px}
  .coupon-package .small{font-size:17px;font-weight:700;margin-top:2px}

  .or{position:absolute;left:342px;top:436px;font-family:"Antonio",sans-serif;font-size:30px;color:var(--teal);font-weight:400}
  .terms{position:absolute;left:330px;top:505px;font-family:"Antonio",sans-serif;font-size:17px;line-height:1.35;color:var(--teal);text-transform:uppercase;text-align:center}
</style>
</head>
<body>
<main class="postcard">
  <div class="pet-photo" role="img" aria-label="Photo of a small Yorkshire terrier looking up to the left"></div>

  <h1 class="headline">GRAND OPENING</h1>

  <section class="event-info">
    <p class="event-date">SEPTEMBER 13</p>
    <p class="event-time">12PM - 4PM</p>
    <p class="event-address">ADRESS STREET 12345</p>
  </section>

  <div class="brand">
    <span class="brand-mark"></span>
    <p class="brand-name">Fern Hollow<br>Animal Hospital</p>
  </div>

  <div class="divider"></div>

  <p class="website">WWW.FERNHOLLOWVETS.COM</p>

  <div class="coupon coupon-free">
    <svg viewBox="0 0 260 240" aria-hidden="true">
      <polyline points="10,80 10,40 60,40" fill="none" stroke="#222" stroke-width="2"/>
      <polyline points="160,10 210,10 230,60" fill="none" stroke="#222" stroke-width="2"/>
      <polyline points="60,230 110,230" fill="none" stroke="#222" stroke-width="2"/>
      <rect x="50" y="40" width="160" height="160" fill="var(--orange)" transform="rotate(-30 130 120)"/>
      <rect x="40" y="38" width="170" height="170" fill="var(--coupon-teal)" transform="rotate(-8 125 123)"/>
    </svg>
    <div class="coupon-text">
      <span class="big">FREE</span>
      <span class="small">OFFICE VISIT</span>
    </div>
  </div>

  <span class="or">OR</span>

  <div class="coupon coupon-package">
    <svg viewBox="0 0 260 240" aria-hidden="true">
      <polyline points="210,10 240,10 250,60" fill="none" stroke="#222" stroke-width="2"/>
      <polyline points="30,230 60,235" fill="none" stroke="#222" stroke-width="2"/>
      <rect x="55" y="40" width="160" height="160" fill="var(--orange)" transform="rotate(28 135 120)"/>
      <rect x="42" y="36" width="170" height="170" fill="var(--coupon-green)" transform="rotate(-10 127 121)"/>
    </svg>
    <div class="coupon-text">
      <span class="amount"><span class="dollar">$</span><span class="big">20</span><span class="off">OFF</span></span>
      <span class="small">OF PACKAGES</span>
    </div>
  </div>

  <p class="terms">For the<br>first time<br>clients.</p>
</main>
</body>
</html>
```